RLT PowerPoint

I am looking for a clean, corporate PowerPoint template.

I would like the following:
- title slide
- break slide
- blank slide with title (for graphs or graphics)
- an ending slide.

Target Market(s)

Business professionals, medium to large business clients.

Requirements
Must have
• Must incorporate the RLT logo in either the header or footer

```html
<!DOCTYPE html>
<html lang="en">
<head>
<meta charset="utf-8">
<title>RLT – Thank You</title>
<link rel="stylesheet" href="https://fonts.googleapis.com/css2?family=Open+Sans:wght@400;600;700&family=Roboto+Condensed:wght@700&family=Patrick+Hand&display=swap">
<style>
  :root {
    --blue-deep: #0052a3;
    --blue-mid: #0a63b5;
    --blue-light: #2a9be0;
    --title-blue: #0b55a8;
    --white: #ffffff;
    --sun-light: #fcc13a;
    --sun-dark: #f4a01c;
  }
  html, body {
    margin: 0;
    padding: 0;
    overflow: hidden;
    background: var(--white);
  }
  .slide {
    position: relative;
    width: 1200px;
    height: 900px;
    overflow: hidden;
    background: var(--white);
    font-family: "Open Sans", sans-serif;
  }
  .header-band {
    position: absolute;
    left: 0; top: 0;
    width: 1200px; height: 80px;
    background: linear-gradient(90deg, var(--blue-deep) 0%, var(--blue-deep) 55%, var(--blue-light) 100%);
    box-shadow: 0 2px 4px rgba(0,0,0,0.25);
  }
  .brand {
    position: absolute;
    right: 44px; top: 20px;
    color: var(--white);
    font-weight: 600;
    font-size: 30px;
    line-height: 40px;
    letter-spacing: 1px;
    white-space: nowrap;
  }
  .emblem-area {
    position: absolute;
    left: 516px; top: 300px;
    width: 134px; height: 134px;
    background: linear-gradient(180deg, var(--sun-light) 0%, var(--sun-dark) 100%);
  }
  .closing-title {
    position: absolute;
    left: 0; top: 442px;
    width: 1168px;
    margin: 0;
    text-align: center;
    font-family: "Roboto Condensed", sans-serif;
    font-weight: 700;
    font-size: 76px;
    line-height: 84px;
    letter-spacing: -2px;
    color: var(--title-blue);
  }
  .closing-sub {
    position: absolute;
    left: 502px; top: 520px;
    margin: 0;
    font-family: "Patrick Hand", cursive;
    font-size: 30px;
    line-height: 36px;
    letter-spacing: 1px;
    color: var(--title-blue);
    white-space: nowrap;
  }
  .footer-band {
    position: absolute;
    left: 0; top: 818px;
    width: 1200px; height: 82px;
    background: linear-gradient(90deg, var(--blue-deep) 0%, var(--blue-mid) 55%, var(--blue-light) 100%);
  }
  .enquiries {
    position: absolute;
    left: 45px; top: 21px;
    color: var(--white);
  }
  .enquiries-label {
    margin: 0;
    font-weight: 700;
    font-size: 17px;
    line-height: 21px;
  }
  .enquiries-contact {
    margin: 0;
    font-weight: 400;
    font-size: 15px;
    line-height: 20px;
  }
  .scroll-hint {
    position: absolute;
    left: 1008px; top: 776px;
    width: 97px; height: 98px;
    background: var(--title-blue);
    color: var(--white);
    display: flex;
    flex-direction: column;
    justify-content: center;
    align-items: center;
    font-size: 18px;
    line-height: 21px;
    text-transform: uppercase;
  }
  .scroll-hint strong { font-weight: 700; }
</style>
</head>
<body>
<main class="slide">
  <header class="header-band">
    <div class="brand">RLT&nbsp;&nbsp;Rowan Lang Advisory</div>
  </header>

  <section class="closing">
    <div class="emblem-area" role="img" aria-label="Glossy orange smiley emoji illustration"></div>
    <h1 class="closing-title">Thank You</h1>
    <p class="closing-sub">FOR YOUR TIME ..!</p>
  </section>

  <footer class="footer-band">
    <div class="enquiries">
      <p class="enquiries-label">For trade enquiries :</p>
      <p class="enquiries-contact">www.rowanlangadvisory.com | info@rowanlangadvisory.com</p>
    </div>
  </footer>

  <div class="scroll-hint">
    <span>Scroll</span>
    <span>Your</span>
    <strong>Mouse</strong>
  </div>
</main>
</body>
</html>
```